Latin CBD company needs a design for a counter display box

-We would like a design for a display box for our restorative CBD oil tinctures. We would like to stand out our brand promoting wellness being and health. However, because its targeting the latin market, we would like to see color on it.
- The display box is for CBD tinctures (image attached)
-I am attaching two files, if you are Spanish speaker it would be nice to see the design in Spanish. Thank you!
THANK YOU IN ADVANCE FOR WORKING IN OUR PROJECT!

Font styles to use
Serif
Sans Serif

```html
<!DOCTYPE html>
<html lang="es">
<head>
<meta charset="utf-8">
<title>Verdora CBD – Caja exhibidora</title>
<link rel="stylesheet" href="https://fonts.googleapis.com/css2?family=Montserrat:wght@500;600&family=Roboto+Condensed:wght@400;700&family=Parisienne&display=swap">
<style>
  :root{
    --green:#0b6a3b;
    --green-dark:#06381f;
    --green-mid:#1e7a45;
    --brown:#6a3c1c;
    --cut:#e8442b;
    --wave:#e4e4e4;
    --white:#ffffff;
  }
  html,body{margin:0;padding:0;overflow:hidden;background:var(--white);}
  .canvas{position:relative;width:1200px;height:1050px;overflow:hidden;background:var(--white);}
  .dieline{position:absolute;left:0;top:0;}
  .brand{position:absolute;text-align:center;color:var(--brown);font-family:"Montserrat",sans-serif;font-weight:600;letter-spacing:.5px;white-space:nowrap;}
  .mark{position:absolute;border:2px solid var(--brown);border-radius:50%;box-sizing:border-box;}
  .mark--light{border-color:var(--white);}
  .pill{position:absolute;background:var(--green);color:var(--white);border-radius:10px;font-family:"Roboto Condensed",sans-serif;font-size:13px;text-align:center;}
  .tagline{position:absolute;left:318px;width:306px;top:765px;text-align:center;font-family:"Parisienne",cursive;color:var(--brown);font-size:21px;line-height:23px;}
  .benefits{position:absolute;margin:0;padding:0;list-style:none;font-family:"Roboto Condensed",sans-serif;font-weight:700;color:var(--white);font-size:11px;line-height:14.5px;}
  .benefits li{margin-bottom:5.5px;}
  .benefits .lead,.benefits .cont{display:block;white-space:nowrap;}
  .benefits--left{left:121px;top:718px;width:190px;}
  .benefits--left .lead::before{content:"• ";}
  .benefits--left .cont{padding-left:10px;}
  .benefits--right{left:630px;top:718px;width:191px;text-align:right;}
  .benefits--right .lead::after{content:" •";}
  .benefits--right .cont{padding-right:10px;}
  .story{position:absolute;left:862px;top:529px;width:240px;font-family:"Roboto Condensed",sans-serif;color:var(--white);font-size:10.6px;line-height:13.2px;text-align:justify;}
  .story p{margin:0 0 7px;}
  .contact{position:absolute;left:862px;top:768px;font-family:"Roboto Condensed",sans-serif;color:var(--white);font-size:7.6px;line-height:11px;letter-spacing:-.2px;}
  .contact strong{display:block;font-size:9.6px;margin-bottom:3px;}
  .web{position:absolute;left:1020px;top:781px;width:82px;text-align:right;font-family:"Roboto Condensed",sans-serif;font-weight:700;color:var(--white);font-size:7.6px;letter-spacing:-.2px;}
  .flip{position:absolute;left:832px;top:300px;width:306px;height:104px;transform:rotate(180deg);}
</style>
</head>
<body>
<div class="canvas">
  <svg class="dieline" width="1200" height="1050" viewBox="0 0 1200 1050">
    <defs>
      <linearGradient id="leafShade" x1="0" y1="0" x2="1" y2="1">
        <stop offset="0" stop-color="#0d3d24"/>
        <stop offset=".45" stop-color="#1f7242"/>
        <stop offset="1" stop-color="#0b5a31"/>
      </linearGradient>
    </defs>
    <polygon points="846,72 1124,72 1138,264 832,264" fill="var(--green)" stroke="var(--cut)" stroke-width="1"/>
    <g role="img" aria-label="Banda decorativa de líneas onduladas grises">
      <rect x="832" y="264" width="306" height="36" fill="var(--wave)"/>
    </g>
    <rect x="832" y="300" width="306" height="104" fill="var(--white)" stroke="var(--cut)" stroke-width="1"/>
    <rect x="832" y="404" width="306" height="104" fill="var(--white)" stroke="var(--cut)" stroke-width="1"/>
    <polygon points="110,508 119,494 119,460 308,460 308,494 318,508" fill="var(--white)" stroke="var(--cut)" stroke-width="1"/>
    <polygon points="624,508 634,494 634,460 822,460 822,494 832,508" fill="var(--white)" stroke="var(--cut)" stroke-width="1"/>
    <g role="img" aria-label="Fotografía de hojas de cáñamo en tonos verdes">
      <polygon points="110,508 62,594 62,762 110,832 318,832 318,508" fill="url(#leafShade)" stroke="var(--cut)" stroke-width="1"/>
    </g>
    <line x1="110" y1="508" x2="110" y2="832" stroke="var(--cut)" stroke-width="1"/>
    <line x1="110" y1="512" x2="318" y2="752" stroke="var(--cut)" stroke-width="1" stroke-dasharray="4 3"/>
    <rect x="318" y="508" width="306" height="324" fill="var(--white)" stroke="var(--cut)" stroke-width="1"/>
    <g role="img" aria-label="Banda decorativa de líneas onduladas grises">
      <rect x="318" y="726" width="306" height="30" fill="var(--wave)"/>
    </g>
    <g role="img" aria-label="Fotografía de hojas de cáñamo en tonos verdes">
      <rect x="624" y="508" width="208" height="324" fill="url(#leafShade)" stroke="var(--cut)" stroke-width="1"/>
    </g>
    <line x1="624" y1="752" x2="832" y2="512" stroke="var(--cut)" stroke-width="1" stroke-dasharray="4 3"/>
    <rect x="832" y="508" width="306" height="324" fill="var(--green)" stroke="var(--cut)" stroke-width="1"/>
    <polygon points="110,832 110,868 169,936 169,972 173,976 254,976 258,972 258,936 318,868 318,832" fill="var(--white)" stroke="var(--cut)" stroke-width="1"/>
    <polygon points="318,832 318,976 558,976 566,968 506,914 624,832" fill="var(--white)" stroke="var(--cut)" stroke-width="1"/>
    <polygon points="624,832 624,976 684,976 684,926 688,922 768,922 772,926 772,976 832,976 832,832" fill="var(--white)" stroke="var(--cut)" stroke-width="1"/>
    <polygon points="832,832 904,914 890,968 898,976 1138,976 1138,832" fill="var(--white)" stroke="var(--cut)" stroke-width="1"/>
    <circle cx="985" cy="799" r="18" fill="var(--white)" stroke="var(--cut)" stroke-width="3"/>
    <circle cx="1048" cy="803" r="7" fill="var(--white)"/>
    <circle cx="1068" cy="803" r="7" fill="var(--white)"/>
    <circle cx="1088" cy="803" r="7" fill="var(--white)"/>
  </svg>

  <div class="mark" style="left:443px;top:593px;width:54px;height:54px;"></div>
  <div class="brand" style="left:318px;width:306px;top:646px;font-size:27px;">VERDORA CBD</div>
  <div class="pill" style="left:410px;top:686px;width:120px;height:18px;line-height:18px;">Hemp Oil Extract</div>
  <div class="tagline">Descubre los beneficios de<br>vivir plenamente saludable</div>

  <div class="mark mark--light" style="left:131px;top:622px;width:57px;height:57px;"></div>
  <ul class="benefits benefits--left">
    <li><span class="lead">100% hecho de plantas naturales</span><span class="cont">cultivadas en Colorado</span></li>
    <li><span class="lead">Fortalece el Sistema</span><span class="cont">Endocananbinoide</span></li>
    <li><span class="lead">Espectro Completo</span></li>
    <li><span class="lead">No psicoactivo</span></li>
  </ul>
  <div class="mark mark--light" style="left:753px;top:622px;width:57px;height:57px;"></div>
  <ul class="benefits benefits--right">
    <li><span class="lead">100% hecho de plantas naturales</span><span class="cont">cultivadas en Colorado</span></li>
    <li><span class="lead">Fortalece el Sistema</span><span class="cont">Endocananbinoide</span></li>
    <li><span class="lead">Espectro Completo</span></li>
    <li><span class="lead">No psicoactivo</span></li>
  </ul>

  <div class="mark" style="left:964px;top:419px;width:42px;height:42px;"></div>
  <div class="brand" style="left:832px;width:306px;top:457px;font-size:21px;">VERDORA CBD</div>
  <div class="pill" style="left:929px;top:485px;width:112px;height:17px;line-height:17px;font-size:12px;">Hemp Oil Extract</div>

  <div class="flip">
    <div class="mark" style="left:133px;top:15px;width:42px;height:42px;"></div>
    <div class="brand" style="left:0;width:306px;top:53px;font-size:21px;">VERDORA CBD</div>
    <div class="pill" style="left:97px;top:81px;width:112px;height:17px;line-height:17px;font-size:12px;">Hemp Oil Extract</div>
  </div>

  <div class="story">
    <p>Verdora CBD es la primer compañía de aceite de CBD dirigida principalmente a la comunidad latina en los Estados Unidos. Nace en el año 2017 ante la necesidad de dar a conocer los beneficios y usos de ésta planta milenaria y terapéutica, que ofrece beneficios extraordinarios para nuestra salud de forma 100% natural, y sin ningún efecto psicoactivo o secundario.</p>
    <p>En Verdora CBD nos sentimos orgullosos de poder brindar la más alta calidad de productos de CBD provenientes de cultivos de plantas orgánicas de Cáñamo en el estado de Colorado, el cual es conocido por sus espectaculares escenarios naturales que incluyen ríos, montañas, mesetas y diferentes ecosistemas naturales. Un lugar que nos ofrece las bondades de sus suelos y altitud perfecta para crecer ésta variedad de planta terapéutica y medicinal.</p>
  </div>
  <div class="contact">
    <strong>VERDORA CBD</strong>
    418 Palma Verde Ave, Suite 5<br>
    Coral Bay, FL 33100 - USA<br>
    <b>Ph: 3055550147</b>
  </div>
  <div class="web">www.verdoracbd.com</div>
</div>
</body>
</html>
```